Business Card and Letterhead for Nurlo - modern real estate business

I need a double sided business card design for Nurlo. Please see business card brief here https://papers.trelvimo.net/sheet/q/7XrTbaLeZpMmQ2uWvd9HkCj4yNoEfsGi3lRtAz_pk/view?mode=shared

Please feel free to design the business cards however you feel best. I am happy to give some creative freedoms and then provide feedback from there.

Please then also create a letterhead to match the business card design

Colors

Designer to choose colors to be used in the design.

Requirements
Must have
• Must be a modern, elegant business card which looks very professional

```html
<!DOCTYPE html>
<html lang="en">
<head>
<meta charset="utf-8">
<title>Nurlo Business Card</title>
<link href="https://fonts.googleapis.com/css2?family=Raleway:wght@400;700;800&display=swap" rel="stylesheet">
<style>
  :root {
    --bg: #ecebe8;
    --card: #231f20;
    --red: #e3161b;
    --white: #ffffff;
    --shadow: rgba(0, 0, 0, 0.25);
  }
  * { box-sizing: border-box; margin: 0; padding: 0; }
  html, body {
    width: 1200px;
    height: 900px;
    overflow: hidden;
    background: var(--bg);
    font-family: "Raleway", sans-serif;
  }
  .canvas {
    width: 1200px;
    height: 900px;
    display: flex;
    flex-direction: column;
    align-items: center;
    justify-content: center;
    gap: 40px;
  }
  .card {
    position: relative;
    width: 680px;
    height: 390px;
    background: var(--card);
    overflow: hidden;
    box-shadow: 0 10px 28px var(--shadow);
  }

  /* Front side */
  .agent-photo {
    position: absolute;
    inset: 0;
    clip-path: polygon(47% 0, 100% 0, 100% 100%, 58% 100%);
    background: linear-gradient(180deg, #f4f5f3 0%, #c9d2d6 28%, #93a58c 55%, #5b6b4c 75%, #2e2b2b 100%);
  }
  .accent-stripe {
    position: absolute;
    inset: 0;
    width: 100%;
    height: 100%;
  }
  .identity {
    position: absolute;
    left: 56px;
    top: 70px;
    color: var(--white);
  }
  .identity .name {
    font-weight: 800;
    font-size: 26px;
    letter-spacing: 0.5px;
  }
  .identity .role {
    font-weight: 400;
    font-size: 19px;
    letter-spacing: 0.5px;
    margin-top: 2px;
  }
  .identity .rule {
    width: 50px;
    height: 7px;
    background: var(--red);
    margin-top: 14px;
  }
  .contact {
    position: absolute;
    left: 76px;
    top: 206px;
    list-style: none;
    color: var(--white);
    font-size: 19px;
    line-height: 27px;
    letter-spacing: 0.8px;
  }

  /* Back side */
  .landscape-band {
    position: absolute;
    left: 0;
    top: 158px;
    width: 280px;
    height: 86px;
    background: linear-gradient(100deg, #2f5fb8 0%, #3a6fc4 14%, #4d7a3a 24%, #3f6a2e 55%, #5c7a45 100%);
  }
  .brand {
    position: absolute;
    left: 306px;
    top: 158px;
    height: 86px;
    display: flex;
    align-items: center;
  }
  .brand .wordmark {
    color: var(--red);
    font-weight: 700;
    font-size: 86px;
    line-height: 1;
    letter-spacing: 4px;
  }
</style>
</head>
<body>
<main class="canvas">
  <section class="card card-front">
    <div class="agent-photo" role="img" aria-label="Portrait photo of the agent in a dark suit outdoors with a valley view behind"></div>
    <svg class="accent-stripe" viewBox="0 0 680 390" preserveAspectRatio="none" aria-hidden="true">
      <polygon points="311,0 321,0 397,390 387,390" fill="var(--red)"/>
    </svg>
    <div class="identity">
      <p class="name">Liam Carter</p>
      <p class="role">Licenced Real Estate Agent</p>
      <div class="rule"></div>
    </div>
    <ul class="contact">
      <li>0400 318 592</li>
      <li>liam@nurlo.com</li>
      <li>PO Box 1190</li>
      <li>Ferndale NSW 2790</li>
      <li>www.nurlo.com</li>
    </ul>
  </section>

  <section class="card card-back">
    <div class="landscape-band" role="img" aria-label="Aerial photo of a river winding beside dense bushland"></div>
    <div class="brand">
      <p class="wordmark">NURLO</p>
    </div>
  </section>
</main>
</body>
</html>
```